Label

I need a label designed for a bottle of water. I like the lightning bolt and the blue. But I do not want it exactly like the Zimm-ooh.

The label needs to be 9 inches by 2.5 inches.

Logo Text

Mesa Spring: Sip the Mesa

```html
<!DOCTYPE html>
<html lang="en">
<head>
<meta charset="utf-8">
<title>Mesa Spring – Bottle Label</title>
<link rel="stylesheet" href="https://fonts.googleapis.com/css2?family=Spectral:wght@400;500&display=swap">
<style>
  :root {
    --page: #ffffff;
    --sky-top: #4169a6;
    --sky-mid: #44608f;
    --sky-bottom: #3a4254;
    --glow: rgba(178, 196, 238, 0.34);
    --glow-soft: rgba(160, 182, 230, 0.16);
    --label-edge: #1d2230;
    --ink: #ffffff;
    --shadow: rgba(0, 0, 0, 0.35);
  }
  * { box-sizing: border-box; margin: 0; padding: 0; }
  html, body {
    width: 1200px;
    height: 441px;
    overflow: hidden;
    background: var(--page);
  }
  .canvas {
    position: relative;
    width: 1200px;
    height: 441px;
  }
  .label {
    position: absolute;
    left: 42px;
    top: 62px;
    width: 1116px;
    height: 310px;
    border: 1px solid var(--label-edge);
    box-shadow: 8px 14px 22px var(--shadow);
    overflow: hidden;
    font-family: "Spectral", Georgia, serif;
    color: var(--ink);
  }
  .label__sky {
    position: absolute;
    inset: 0;
    background: linear-gradient(180deg, var(--sky-top) 0%, var(--sky-mid) 50%, var(--sky-bottom) 100%);
  }
  .label__storm {
    position: absolute;
    inset: 0;
    background:
      radial-gradient(ellipse 90px 260px at 300px 120px, var(--glow) 0%, transparent 70%),
      radial-gradient(ellipse 60px 200px at 250px 260px, var(--glow-soft) 0%, transparent 70%),
      radial-gradient(ellipse 320px 70px at 960px 90px, var(--glow) 0%, transparent 70%),
      radial-gradient(ellipse 260px 60px at 800px 180px, var(--glow-soft) 0%, transparent 70%),
      radial-gradient(ellipse 120px 40px at 1090px 20px, var(--glow) 0%, transparent 75%);
  }
  .brand {
    position: absolute;
    inset: 0;
    text-align: center;
  }
  .brand__mark {
    position: absolute;
    left: 510px;
    top: 36px;
    width: 62px;
    height: 62px;
    border-radius: 50%;
    background: var(--ink);
  }
  .brand__name {
    position: absolute;
    left: 0;
    right: 32px;
    top: 136px;
    font-size: 70px;
    font-weight: 500;
    line-height: 1;
    letter-spacing: 0;
    text-transform: uppercase;
  }
  .brand__tagline {
    position: absolute;
    left: 0;
    right: 32px;
    top: 213px;
    font-size: 37px;
    font-weight: 500;
    line-height: 1;
    text-transform: uppercase;
  }
  .volume {
    position: absolute;
    right: 12px;
    bottom: 10px;
    font-size: 23px;
    font-weight: 400;
    line-height: 1;
  }
</style>
</head>
<body>
  <div class="canvas">
    <div class="label">
      <div class="label__sky"></div>
      <div class="label__storm" role="img" aria-label="Stormy blue sky with branching lightning bolts across the left and upper right"></div>
      <div class="brand">
        <span class="brand__mark" aria-hidden="true"></span>
        <h1 class="brand__name">Mesa Spring</h1>
        <p class="brand__tagline">Sip the Mesa</p>
      </div>
      <p class="volume">1 Liter (33.8 fl. oz)</p>
    </div>
  </div>
</body>
</html>
```